Looking for awesome business card design with attached existing logo

We are a water, mold, and fire damage restoration company called "Torvane Seco" Looking for an awesome business card that is edgy yet professional and unique. Show me what you got!

```html
<!DOCTYPE html>
<html lang="en">
<head>
<meta charset="utf-8">
<title>Torvane Seco — Business Card</title>
<link href="https://fonts.googleapis.com/css2?family=Montserrat:wght@400;500;700;800&display=swap" rel="stylesheet">
<style>
  :root {
    --teal-dark: #2b4753;
    --teal-back: #2e4b58;
    --teal-light: #4a9cc0;
    --gold: #d99a2b;
    --red: #c4252c;
    --ink: #3c3c3c;
    --paper: #ffffff;
    --stage: #1c1c1e;
  }
  * { margin: 0; padding: 0; box-sizing: border-box; }
  html, body { width: 1200px; height: 900px; overflow: hidden; }
  body {
    background: var(--stage);
    font-family: "Montserrat", Arial, sans-serif;
    position: relative;
  }
  .card {
    position: absolute;
    left: 250px;
    width: 700px;
    height: 400px;
    border-radius: 4px;
    overflow: hidden;
    box-shadow: 0 14px 30px rgba(0,0,0,.45);
  }
  .card--front { top: 30px; background: var(--paper); }
  .card--back { top: 465px; background: var(--teal-back); display: flex; align-items: center; justify-content: center; }

  .front__wave { position: absolute; inset: 0; width: 700px; height: 400px; }

  .brand {
    position: absolute;
    left: 56px;
    top: 112px;
    display: flex;
    align-items: center;
    gap: 14px;
  }
  .brand__dot { width: 18px; height: 18px; border-radius: 50%; background: var(--gold); flex: none; }
  .brand__name {
    font-weight: 800;
    font-size: 40px;
    line-height: 1.05;
    letter-spacing: 1px;
    color: var(--teal-dark);
    text-transform: uppercase;
  }

  .divider {
    position: absolute;
    left: 345px;
    top: 110px;
    width: 1.5px;
    height: 200px;
    background: var(--teal-dark);
  }

  .contact {
    position: absolute;
    left: 372px;
    top: 108px;
    color: var(--ink);
  }
  .contact__name {
    font-weight: 800;
    font-size: 22px;
    color: var(--teal-dark);
    text-transform: uppercase;
    letter-spacing: .5px;
  }
  .contact__role {
    font-weight: 500;
    font-size: 16px;
    color: var(--gold);
    margin-bottom: 14px;
  }
  .contact__address { font-size: 15px; line-height: 1.35; margin-bottom: 10px; }
  .contact__list { list-style: none; font-size: 15px; line-height: 1.55; }
  .contact__list li { display: flex; align-items: center; gap: 8px; }
  .contact__icon { width: 13px; height: 13px; flex: none; fill: var(--red); }

  .back__brand { display: flex; align-items: center; gap: 18px; }
  .back__dot { width: 30px; height: 30px; border-radius: 50%; background: var(--teal-light); flex: none; }
  .back__name {
    font-weight: 800;
    font-size: 58px;
    letter-spacing: 2px;
    color: var(--teal-light);
    text-transform: uppercase;
  }
</style>
</head>
<body>

<section class="card card--front">
  <svg class="front__wave" viewBox="0 0 700 400" aria-hidden="true">
    <path d="M0,262 C170,270 300,320 460,375 C560,405 640,400 700,398 L700,400 L0,400 Z" fill="var(--teal-dark)"/>
    <path d="M0,256 C170,262 300,312 460,366 C560,396 640,392 700,390" fill="none" stroke="var(--red)" stroke-width="7"/>
    <path d="M0,251 C170,256 300,306 460,360 C560,390 640,386 700,384" fill="none" stroke="var(--gold)" stroke-width="2"/>
  </svg>

  <div class="brand">
    <span class="brand__dot"></span>
    <span class="brand__name">Torvane<br>Seco</span>
  </div>

  <div class="divider"></div>

  <div class="contact">
    <p class="contact__name">Marcus Delane</p>
    <p class="contact__role">President</p>
    <p class="contact__address">1850 Harbor Crest Dr<br>Seaview CA 90210</p>
    <ul class="contact__list">
      <li>
        <svg class="contact__icon" viewBox="0 0 24 24"><path d="M6.6 10.8a15.1 15.1 0 0 0 6.6 6.6l2.2-2.2a1 1 0 0 1 1-.25 11.4 11.4 0 0 0 3.6.57 1 1 0 0 1 1 1V20a1 1 0 0 1-1 1A17 17 0 0 1 3 4a1 1 0 0 1 1-1h3.5a1 1 0 0 1 1 1c0 1.25.2 2.45.57 3.6a1 1 0 0 1-.25 1z"/></svg>
        555-014-2873
      </li>
      <li>
        <svg class="contact__icon" viewBox="0 0 24 24"><path d="M2 5h20v14H2z M2 5l10 8 10-8" stroke="#fff" stroke-width="1.5"/></svg>
        marcusdelane@torvaneseco.com
      </li>
      <li>
        <svg class="contact__icon" viewBox="0 0 24 24"><circle cx="12" cy="12" r="10"/><path d="M2 12h20M12 2c3 3 3 17 0 20M12 2c-3 3-3 17 0 20" fill="none" stroke="#fff" stroke-width="1.3"/></svg>
        www.torvaneseco.com
      </li>
    </ul>
  </div>
</section>

<section class="card card--back">
  <div class="back__brand">
    <span class="back__dot"></span>
    <span class="back__name">Torvane Seco</span>
  </div>
</section>

</body>
</html>
```